A start up special flyer design!

Hi All - Have updated the attachment content - This is the info required for the designs.
I need a catchy flyer to send out to a few areas to advertise the start of my plumbing business!
The flyer will contain an offer for customers, which will need to have some key details on it. See attached. Feel free to fit these criteria into the flyer given your knowledge on design and messaging principles. Key thing to get across to customers is the discount and special offer, and that it is a start up offer.
I have a logo that needs to be on the flyer as well - let me know what format you require and I will send through to you.
The color scheme needs to be blue / grey / black / white.
Let me know if you have any questions.
I

```html
<!DOCTYPE html>
<html lang="en">
<head>
<meta charset="utf-8">
<title>Danny Flow Plumbing – Start Up Offer</title>
<link href="https://fonts.googleapis.com/css2?family=Roboto+Condensed:wght@400;700&family=Roboto:wght@400;700&display=swap" rel="stylesheet">
<style>
  :root{
    --blue:#1d4586;
    --blue-deep:#0f4a8f;
    --brand-blue:#2a6db4;
    --sky:#8ed2f7;
    --orange:#ef9435;
    --grey:#7d8287;
    --paper:#e6e9ec;
    --white:#ffffff;
    --ink:#111111;
    --stage:#d8d5d1;
  }
  *{box-sizing:border-box;margin:0;padding:0}
  html,body{width:1200px;height:1000px;overflow:hidden}
  body{background:var(--stage);font-family:"Roboto Condensed",Arial,sans-serif;position:relative}

  /* ---------- Flyer ---------- */
  .flyer{position:absolute;left:40px;top:50px;width:638px;height:900px;overflow:hidden;
    background:linear-gradient(180deg,#e1e5e9 0%,#eef0f2 70%,var(--white) 87%);box-shadow:0 3px 10px rgba(0,0,0,.25)}
  .flyer__wedge{position:absolute;left:0;top:0}
  .flyer__bar{position:absolute;left:250px;top:262px;width:388px;height:20px;background:var(--blue)}
  .flyer__hero{position:absolute;left:35px;top:15px;width:225px;height:460px;border-radius:60px 60px 10px 10px;
    background:linear-gradient(180deg,#f1c54a 0%,#e6d3c0 14%,#3d6fb0 30%,#2f5a96 62%,#b88a52 80%,#6e88a8 100%)}
  .brand{position:absolute;left:250px;top:138px;width:358px;text-align:center;color:var(--brand-blue);
    font-weight:700;letter-spacing:1px;line-height:1.05}
  .brand__name{font-size:38px}
  .brand__sub{font-size:22px;letter-spacing:8px}
  .shot{position:absolute;top:307px;width:176px;height:132px;border:5px solid var(--white);box-shadow:0 1px 4px rgba(0,0,0,.25)}
  .shot--sink{left:247px;background:linear-gradient(135deg,#e9edf1 0%,#7d9cc6 45%,#3a5f95 100%)}
  .shot--pipe{left:432px;background:linear-gradient(135deg,#f2f2f2 0%,#c9cdd2 45%,#d84a3e 75%,#e9c7a9 100%)}

  .panel{position:absolute;top:477px;width:300px;height:253px;background:var(--blue);border-radius:14px;
    border:2px dashed rgba(255,255,255,.7);outline:3px solid var(--blue)}
  .panel--offer{left:2px;border-top-left-radius:0;border-bottom-left-radius:0}
  .panel--services{left:338px;border-top-right-radius:0;border-bottom-right-radius:0}
  .tag{position:absolute;top:-6px;height:38px;background:var(--orange);color:var(--white);font-weight:700;font-size:27px;
    line-height:38px;padding:0 10px;border-radius:4px}
  .panel--offer .tag{left:38px}
  .panel--services .tag{left:37px}

  .deal{position:absolute;left:62px;top:42px;display:flex;align-items:center;color:var(--white)}
  .deal__pct{font-family:Roboto,Arial,sans-serif;font-weight:700;font-size:80px;letter-spacing:-2px;line-height:1}
  .deal__off{font-weight:700;font-size:26px;transform:rotate(90deg);margin-left:-4px;letter-spacing:1px}
  .deal__note{position:absolute;left:0;width:300px;top:124px;text-align:center;color:var(--sky);font-size:17px}
  .ticks{list-style:none;position:absolute;color:var(--sky);font-size:23px;line-height:1.22}
  .ticks li{position:relative;padding-left:30px}
  .ticks svg{position:absolute;left:0;top:2px}
  .panel--offer .ticks{left:16px;top:154px;width:280px}
  .panel--services .ticks{left:16px;top:54px;width:280px}
  .panel--services .ticks li{margin-bottom:26px}

  .flyer__rule{position:absolute;left:0;top:780px;width:638px;height:5px;background:var(--blue)}
  .flyer__foot{position:absolute;left:0;top:785px;width:638px;height:115px;background:var(--white)}
  .cta{position:absolute;left:123px;top:761px;width:393px;height:49px;background:var(--ink);border-radius:7px;color:var(--white);
    font-family:Roboto,Arial,sans-serif;font-size:15px;text-align:center;line-height:21px;padding-top:4px}
  .cta em{font-style:normal;color:var(--sky)}
  .fine{position:absolute;left:46px;top:832px;font-family:Roboto,Arial,sans-serif;font-size:10.5px;font-style:italic;line-height:16px;color:var(--ink)}
  .fine b{font-weight:700}
  .contact{position:absolute;left:390px;top:824px;width:220px;text-align:right;font-family:Roboto,Arial,sans-serif;color:var(--ink)}
  .contact__phone{display:flex;align-items:center;justify-content:flex-end;gap:6px;font-family:"Roboto Condensed",Arial,sans-serif;font-weight:700;font-size:26px}
  .contact__line{font-size:11px;line-height:15px;padding-right:10px}

  /* ---------- Business cards ---------- */
  .card{position:absolute;left:740px;width:386px;overflow:hidden;box-shadow:0 3px 8px rgba(0,0,0,.3)}
  .card--front{top:248px;height:228px;background:var(--blue-deep);color:var(--white);text-align:center}
  .card--front .card__brand{position:absolute;left:0;width:100%;top:103px;font-weight:700;line-height:1.05;letter-spacing:1px}
  .card__brand-name{font-size:28px}
  .card__brand-sub{font-size:16px;letter-spacing:7px}
  .card__services{position:absolute;left:0;width:100%;top:198px;font-size:11.5px;letter-spacing:.3px}
  .card--back{top:533px;height:231px;background:var(--white)}
  .card--back .card__brand{position:absolute;left:22px;top:66px;width:178px;text-align:center;color:var(--brand-blue);font-weight:700;line-height:1.05;letter-spacing:.5px}
  .card--back .card__brand-name{font-size:19px}
  .card--back .card__brand-sub{font-size:11px;letter-spacing:5px}
  .card__details{position:absolute;left:22px;top:144px;list-style:none;font-family:Roboto,Arial,sans-serif;font-size:10px;line-height:18px;color:var(--ink)}
  .card__details li{display:flex;align-items:center;gap:6px}
  .card__stripe{position:absolute;left:0;bottom:0}
</style>
</head>
<body>

<article class="flyer">
  <svg class="flyer__wedge" width="80" height="360" viewBox="0 0 80 360" aria-hidden="true">
    <polygon points="0,185 75,215 75,345 0,345" fill="#1d4586"/>
  </svg>
  <div class="flyer__bar"></div>
  <div class="flyer__hero" role="img" aria-label="Photo of a smiling plumber in a hard hat and blue shirt with arms crossed and a tool belt"></div>

  <div class="brand">
    <div class="brand__name">DANNY FLOW</div>
    <div class="brand__sub">PLUMBING</div>
  </div>

  <div class="shot shot--sink" role="img" aria-label="Photo of a plumber repairing pipes under a sink"></div>
  <div class="shot shot--pipe" role="img" aria-label="Photo of a hand tightening a chrome pipe with a red wrench"></div>

  <section class="panel panel--offer">
    <span class="tag">Offer</span>
    <div class="deal">
      <span class="deal__pct">15%</span><span class="deal__off">OFF</span>
    </div>
    <p class="deal__note">YOUR OVERALL BILL*</p>
    <ul class="ticks">
      <li><svg width="24" height="22" viewBox="0 0 24 22"><path d="M2 12 L9 19 L22 2" fill="none" stroke="#fff" stroke-width="3.5"/></svg>Plus, a free hot water heater health check and replacement quote**</li>
    </ul>
  </section>

  <section class="panel panel--services">
    <span class="tag">Services Offered</span>
    <ul class="ticks">
      <li><svg width="24" height="22" viewBox="0 0 24 22"><path d="M2 12 L9 19 L22 2" fill="none" stroke="#fff" stroke-width="3.5"/></svg>All plumbing, draining, and gasfitting works</li>
      <li><svg width="24" height="22" viewBox="0 0 24 22"><path d="M2 12 L9 19 L22 2" fill="none" stroke="#fff" stroke-width="3.5"/></svg>Quality work at a Decent Price</li>
      <li><svg width="24" height="22" viewBox="0 0 24 22"><path d="M2 12 L9 19 L22 2" fill="none" stroke="#fff" stroke-width="3.5"/></svg>Local Plumber</li>
    </ul>
  </section>

  <div class="flyer__foot"></div>
  <div class="flyer__rule"></div>
  <p class="cta">To make an appointment, <em>call or email Danny</em>,<br>or alternatively make a booking directly on the website</p>

  <p class="fine">*Offer expires <b>31 October 2016</b><br>**Quote valid for <b>12 months</b> from the quote</p>

  <div class="contact">
    <div class="contact__phone">
      <svg width="22" height="22" viewBox="0 0 22 22" aria-hidden="true"><circle cx="11" cy="11" r="9.5" fill="none" stroke="#2a6db4" stroke-width="2"/><path d="M7.5 6 l2 0 l1 3 -1.3 1 a7 7 0 0 0 3 3 l1-1.3 3 1 0 2 a1.5 1.5 0 0 1-1.5 1.3 A9 9 0 0 1 6.3 7.5 1.5 1.5 0 0 1 7.5 6z" fill="#2a6db4"/></svg>
      0400 182 640
    </div>
    <div class="contact__line">danny@dannyflowplumbing.com</div>
    <div class="contact__line">www.dannyflowplumbing.com</div>
  </div>
</article>

<section class="card card--front">
  <div class="card__brand">
    <div class="card__brand-name">DANNY FLOW</div>
    <div class="card__brand-sub">PLUMBING</div>
  </div>
  <p class="card__services">PLUMBING &nbsp;•&nbsp; DRAINING &nbsp;•&nbsp; GASFITTING WORKS</p>
</section>

<section class="card card--back">
  <div class="card__brand">
    <div class="card__brand-name">DANNY FLOW</div>
    <div class="card__brand-sub">PLUMBING</div>
  </div>
  <ul class="card__details">
    <li><svg width="11" height="11" viewBox="0 0 22 22"><circle cx="11" cy="11" r="9.5" fill="none" stroke="#111" stroke-width="2"/><path d="M7.5 6 l2 0 l1 3 -1.3 1 a7 7 0 0 0 3 3 l1-1.3 3 1 0 2 a1.5 1.5 0 0 1-1.5 1.3 A9 9 0 0 1 6.3 7.5 1.5 1.5 0 0 1 7.5 6z" fill="#111"/></svg>0400 182 640</li>
    <li><svg width="11" height="11" viewBox="0 0 22 22"><rect x="2" y="5" width="18" height="12" fill="none" stroke="#111" stroke-width="2"/><path d="M2 5 L11 12 L20 5" fill="none" stroke="#111" stroke-width="2"/></svg>danny@dannyflowplumbing.com</li>
    <li><svg width="11" height="11" viewBox="0 0 22 22"><circle cx="11" cy="11" r="9" fill="none" stroke="#111" stroke-width="2"/><ellipse cx="11" cy="11" rx="4" ry="9" fill="none" stroke="#111" stroke-width="1.6"/><path d="M2 11 H20" stroke="#111" stroke-width="1.6"/></svg>www.dannyflowplumbing.com</li>
  </ul>
  <svg class="card__stripe" width="386" height="22" viewBox="0 0 386 22" aria-hidden="true">
    <polygon points="0,2 200,2 192,22 0,22" fill="#0f4a8f"/>
    <polygon points="206,2 386,2 386,22 198,22" fill="#6d7074"/>
  </svg>
</section>

</body>
</html>
```